The Lanternwork (a book about how to use the Freemasons tools in your everyday life)

This is a book about how to use in real life The ropes that Freemasons study in their allegories. It´s Freemasonry for people who are not initiated but they can use these metaphors about the square, the compass, the gavel, the level, etc in their life for becoming more productive and successful.

please note: this is not another book about freemasonry, or dedicated only to masons... it´s for mothers, workers, bus drivers, CEOs, students and professors. Everybody can take advantage in their lives of using this tools.

book covers to be considered:
Q-Doubled by Lia Brenhold
The ropes by Rudi Kemble
The weight of dawn by R Vashby

in the cover there must me this information:"How to use the philosophy of Freemasonry in your life" Added Thursday, April 16, 2015

Target Market(s)

people who read Delmont, Renato Vilhar, Ruvik.
people who likes books about Self Help
and of course, for freemasons also

Font styles to use
Serif

Requirements
Must have
• the title: The Lanternwork
• my name: Lorenzo Brisca
• additional information: "how to use the philosophy of Freemasonry in your everyday life"
Nice to have
• words like: Success, Motivation, etc
• masonic words like: Square, compass, gavel, level, etc

```html
<!DOCTYPE html>
<html lang="en">
<head>
<meta charset="utf-8">
<title>The Lanternwork — Lorenzo Brisca</title>
<link rel="stylesheet" href="https://fonts.googleapis.com/css2?family=Oswald:wght@500;600&family=Questrial&display=swap">
<style>
  :root {
    --backdrop: #9a9a9a;
    --backdrop-light: #b4b4b4;
    --cover-dark: #38383a;
    --spine-dark: #29292b;
    --lime: #d7f50f;
    --ink: #2b2b2b;
  }
  * { margin: 0; padding: 0; box-sizing: border-box; }
  html, body { width: 1200px; height: 795px; overflow: hidden; }
  body {
    background: radial-gradient(ellipse at 60% 20%, var(--backdrop-light), var(--backdrop) 70%);
    display: flex; align-items: center; justify-content: center;
  }
  .cover {
    position: relative;
    width: 480px; height: 690px;
    background: var(--cover-dark);
    overflow: hidden;
    box-shadow: 0 14px 40px rgba(0,0,0,.25);
  }
  .cover__hinge {
    position: absolute; left: 0; top: 0; bottom: 0; width: 42px;
    background: var(--spine-dark);
    border-right: 1px solid #222;
  }
  .band {
    position: absolute; left: 0; right: 0;
    background: var(--lime);
    display: flex; align-items: center; justify-content: center;
  }
  .band--author { top: 62px; height: 88px; }
  .band--subtitle { top: 450px; bottom: 0; align-items: flex-start; padding-top: 92px; }
  .author {
    font-family: "Oswald", sans-serif; font-weight: 600;
    font-size: 26px; letter-spacing: 9px; color: var(--ink);
    text-transform: uppercase; padding-left: 30px;
  }
  .subtitle {
    font-family: "Oswald", sans-serif; font-weight: 500;
    font-size: 13px; line-height: 1.7; letter-spacing: 4px;
    color: var(--ink); text-transform: uppercase; text-align: center;
    padding-left: 30px;
  }
  .title-frame {
    position: absolute; left: 90px; top: 236px; width: 340px; height: 150px;
  }
  .title-frame svg { position: absolute; inset: 0; }
  .title {
    position: absolute; inset: 0;
    display: flex; flex-direction: column; justify-content: center;
    font-family: "Questrial", sans-serif; color: var(--lime);
    padding-left: 44px;
  }
  .title__the { font-size: 34px; line-height: 1; padding-left: 28px; }
  .title__main { font-size: 46px; line-height: 1.05; letter-spacing: -1px; }
</style>
</head>
<body>
  <main class="cover">
    <div class="cover__hinge"></div>
    <div class="band band--author"><p class="author">Lorenzo Brisca</p></div>
    <div class="title-frame">
      <svg viewBox="0 0 340 150" fill="none" stroke="var(--lime)" stroke-width="1.2">
        <rect x="1" y="1" width="338" height="148"/>
        <rect x="22" y="18" width="296" height="114"/>
        <line x1="1" y1="1" x2="22" y2="18"/>
        <line x1="339" y1="1" x2="318" y2="18"/>
        <line x1="1" y1="149" x2="22" y2="132"/>
        <line x1="339" y1="149" x2="318" y2="132"/>
      </svg>
      <h1 class="title"><span class="title__the">The</span><span class="title__main">Lanternwork</span></h1>
    </div>
    <div class="band band--subtitle">
      <p class="subtitle">How to use the philosophy of Freemasonry<br>in your everyday life</p>
    </div>
  </main>
</body>
</html>
```